Helicopter Company - Skyvane Sweden

I need a new design and implementation of a webpage. We rent helicopters and are also starting a school. We havre started a wordpress but the page is very ugly. Need a complete update. Logo exist already. We also have some pictures of helicotopers. We are open for all designs but it is important that it looks professionel, is eassy to update and will give an impression och structure and dicipline.
Updates

Target Market(s)

Customers that what to get a certificate to fly. It is expensive so it’s either people with a lot of money or people with a big dream. It is very serious business.

Industry/Entity Type

www.skyvane-demo.se

Coding

Coded - Design and coding required

Number of Pages Required

4 page

Font styles to use
Sans Serif

Colors
0054AA
0677BA
7BADD7
CADEEF
E8F1F8

Requirements
Must have
• A easy page the gives a feeling of seriousness and

```html
<!DOCTYPE html>
<html lang="en">
<head>
<meta charset="utf-8">
<title>Skyvane – Helicopter Rental</title>
<link href="https://fonts.googleapis.com/css2?family=Poppins:wght@300;400;500;600;700&display=swap" rel="stylesheet">
<style>
:root{
  --blue-900:#0054AA;
  --blue-700:#0677BA;
  --blue-400:#7BADD7;
  --blue-200:#CADEEF;
  --blue-100:#E8F1F8;
  --white:#ffffff;
  --navy:#003f80;
  --ink:#123a63;
  --text:#4f6477;
  --footer-text:#dce9f5;
}
*{margin:0;padding:0;box-sizing:border-box}
html,body{width:1200px;height:2444px;overflow:hidden}
body{position:relative;background:var(--white);font-family:'Poppins',Arial,sans-serif;color:var(--text)}
.abs{position:absolute}

.intro-bg{position:absolute;left:0;top:0;width:1200px;height:1314px;background:var(--blue-100)}
.hero{position:absolute;left:0;top:0}

.logo{left:160px;top:46px;display:flex;align-items:center;gap:10px;font-size:28px;font-weight:600;letter-spacing:2px;color:var(--blue-900);line-height:1}
.logo-mark{width:12px;height:12px;border-radius:50%;background:var(--blue-900)}
.nav{top:56px;font-size:14px;font-weight:400;color:var(--ink);line-height:1}
.nav.active{font-weight:600;color:var(--blue-900)}
.social-ring{top:46px;width:36px;height:36px;border:1.5px solid var(--blue-900);border-radius:50%}

.eyebrow{left:0;width:1200px;text-align:center;font-size:21px;font-weight:400;color:var(--blue-700);line-height:1.2}
.display{left:0;width:1200px;text-align:center;font-size:54px;font-weight:700;letter-spacing:1px;color:var(--blue-900);line-height:1}

.about{left:160px;top:905px;width:520px;display:flex;flex-direction:column;align-items:flex-start}
.about-title{font-size:30px;font-weight:600;line-height:36px;color:var(--ink)}
.about-copy{margin-top:22px;width:515px;font-size:12.5px;line-height:23.3px;font-weight:300;color:var(--text)}
.btn{height:45px;width:141px;border:1.5px solid var(--blue-400);border-radius:23px;display:flex;align-items:center;justify-content:center;gap:10px;font-size:13px;font-weight:600;color:var(--blue-700);line-height:1}
.btn svg{width:14px;height:8px}
.about .btn{margin-top:28px}
.about-photo{left:698px;top:908px;width:344px;height:320px;border:3px solid var(--white);background:radial-gradient(ellipse at 70% 45%,#5f7382 0%,#8797a3 30%,transparent 60%),linear-gradient(180deg,#eef1f4 0%,#dfe4e8 60%,#b9c2c9 100%)}

.intro-copy{left:300px;top:1462px;width:600px;text-align:center;font-size:13px;line-height:19px;font-weight:300;color:var(--text)}

.card-photo{width:276px}
.photo-alps{left:160px;top:1598px;height:263px;background:radial-gradient(ellipse at 45% 62%,#c8202a 0%,#c8202a 12%,transparent 28%),linear-gradient(180deg,#8fa7c4 0%,#dde4ec 30%,#5b6b55 55%,#4a4d52 72%,#393b3f 100%)}
.photo-tarmac{left:462px;top:1532px;height:329px;background:radial-gradient(ellipse at 50% 50%,#e3c21e 0%,#d2342a 14%,transparent 30%),linear-gradient(180deg,#7f9cd2 0%,#cfd2e6 35%,#8b8c8a 60%,#5c5a58 100%)}
.photo-blue{left:764px;top:1598px;height:263px;background:radial-gradient(ellipse at 55% 60%,#eef0f3 0%,#cfd5dc 14%,transparent 30%),linear-gradient(180deg,#0e2a56 0%,#1f4a86 50%,#7e858e 75%,#5f646b 100%)}
.card-title{width:276px;text-align:center;font-size:21px;font-weight:500;line-height:24px;color:var(--ink)}
.card-copy{top:1958px;width:276px;text-align:center;font-size:11.5px;line-height:18.5px;font-weight:300;letter-spacing:-.1px;color:var(--text)}

.footer{left:0;top:2162px;width:1200px;height:282px;background:var(--blue-900)}
.footer-rule{left:0;top:2338px;width:1200px;height:1px;background:var(--blue-700)}
.contact-col{top:2212px;width:240px;text-align:center;color:var(--footer-text)}
.contact-col svg{display:block;margin:0 auto}
.contact-label{margin-top:10px;font-size:16px;font-weight:600;letter-spacing:4px;color:var(--white)}
.contact-info{margin-top:10px;font-size:9px;font-weight:500;letter-spacing:.3px}
.foot-link{top:2379px;font-size:9px;font-weight:500;color:var(--footer-text)}
.social-box{top:2367px;width:36px;height:36px;border:2px solid var(--white);border-radius:3px}
.copyright{left:823px;top:2379px;font-size:9px;font-weight:500;color:var(--footer-text)}
</style>
</head>
<body>

<div class="intro-bg"></div>

<svg class="hero" width="1200" height="720" viewBox="0 0 1200 720">
  <defs>
    <linearGradient id="heroPhoto" x1="0" y1="0" x2="0" y2="1">
      <stop offset="0" stop-color="#cfdcec"/>
      <stop offset=".4" stop-color="#a9bdd4"/>
      <stop offset=".6" stop-color="#8c9299"/>
      <stop offset=".8" stop-color="#6d7758"/>
      <stop offset="1" stop-color="#55683a"/>
    </linearGradient>
    <radialGradient id="heroSubject" cx=".62" cy=".52" r=".28">
      <stop offset="0" stop-color="#f2f3f5"/>
      <stop offset=".45" stop-color="#d44a4a" stop-opacity=".55"/>
      <stop offset="1" stop-color="#d44a4a" stop-opacity="0"/>
    </radialGradient>
  </defs>
  <g role="img" aria-label="Photo of helicopters parked on an airfield runway">
    <path d="M0 0 H1200 V330 Q500 680 0 578 Z" fill="url(#heroPhoto)"/>
    <path d="M0 0 H1200 V330 Q500 680 0 578 Z" fill="url(#heroSubject)"/>
  </g>
  <path d="M0 585 Q560 740 1200 595 L1200 330 Q500 680 0 578 Z" fill="var(--blue-700)"/>
  <path d="M0 578 Q500 680 1200 330" fill="none" stroke="var(--white)" stroke-width="4"/>
  <path d="M0 586 Q560 740 1200 596" fill="none" stroke="var(--white)" stroke-width="2"/>
</svg>

<div class="abs logo"><span class="logo-mark"></span><span>SKYVANE</span></div>
<div class="abs nav active" style="left:638px">Home</div>
<div class="abs nav" style="left:747px">About us</div>
<div class="abs nav" style="left:873px">Contact</div>
<div class="abs social-ring" style="left:960px" aria-label="Social link"></div>
<div class="abs social-ring" style="left:1003px" aria-label="Social link"></div>

<div class="abs eyebrow" style="top:769px">Welcome to</div>
<div class="abs display" style="top:802px">SKYVANE</div>

<section class="abs about">
  <h2 class="about-title">Providing solutions for<br>construction,management,<br>and restoration.</h2>
  <p class="about-copy">We are a long-established, independent building services and home improvements company. We have a wealth of experience working as main building contractors on all kinds of projects, big and small, from home maintenance and improvements to extensions, refurbishments and new We are a long-established, independent uilding services and home improvements company.</p>
  <div class="btn">READ MORE <svg viewBox="0 0 14 8"><path d="M0 4H12M9 1L12.5 4L9 7" stroke="currentColor" stroke-width="1.6" fill="none"/></svg></div>
</section>
<div class="abs about-photo" role="img" aria-label="Photo of passengers boarding a helicopter on a snowy helipad"></div>

<div class="abs eyebrow" style="top:1364px">Rent your Helicopter</div>
<div class="abs display" style="top:1393px">WE OFFER</div>
<p class="abs intro-copy">We are a long-established, independent building services and home improvements company. We have a wealth of experience working as main building contractors on .</p>

<div class="abs card-photo photo-alps" role="img" aria-label="Photo of a red helicopter on a helipad in the mountains"></div>
<div class="abs card-photo photo-tarmac" role="img" aria-label="Photo of a red and yellow helicopter on tarmac"></div>
<div class="abs card-photo photo-blue" role="img" aria-label="Photo of a white helicopter under a deep blue sky"></div>

<h3 class="abs card-title" style="left:164px;top:1898px">Rental</h3>
<h3 class="abs card-title" style="left:466px;top:1898px">Our Helicopters !</h3>
<h3 class="abs card-title" style="left:768px;top:1889px">Other Types<br>of Helicopter Jobs</h3>

<p class="abs card-copy" style="left:160px">We are a long-established, independent building services and home provements company. We have a wealth of perience working.</p>
<p class="abs card-copy" style="left:462px">We are a long-established, independent building services and home provements company. We have a wealth of perience working.</p>
<p class="abs card-copy" style="left:764px">We are a long-established, independent building services and home provements company. We have a wealth of perience working.</p>

<div class="abs btn" style="left:220px;top:2038px">READ MORE <svg viewBox="0 0 14 8"><path d="M0 4H12M9 1L12.5 4L9 7" stroke="currentColor" stroke-width="1.6" fill="none"/></svg></div>
<div class="abs btn" style="left:521px;top:2038px">READ MORE <svg viewBox="0 0 14 8"><path d="M0 4H12M9 1L12.5 4L9 7" stroke="currentColor" stroke-width="1.6" fill="none"/></svg></div>
<div class="abs btn" style="left:823px;top:2038px">READ MORE <svg viewBox="0 0 14 8"><path d="M0 4H12M9 1L12.5 4L9 7" stroke="currentColor" stroke-width="1.6" fill="none"/></svg></div>

<footer class="abs footer"></footer>
<div class="abs footer-rule"></div>

<div class="abs contact-col" style="left:187px">
  <svg width="24" height="30" viewBox="0 0 24 30"><path d="M12 1C6 1 2 5.5 2 11c0 7 10 18 10 18s10-11 10-18C22 5.5 18 1 12 1Z" fill="var(--white)"/><circle cx="12" cy="11" r="4" fill="var(--blue-900)"/></svg>
  <div class="contact-label">LOCATION</div>
  <div class="contact-info">SKYVANE, NORRBY AIRFIELD,</div>
</div>
<div class="abs contact-col" style="left:480px">
  <svg width="30" height="30" viewBox="0 0 30 30" fill="none" stroke="var(--white)" stroke-width="1.6"><path d="M6 4l5 1 2 6-3 2c2 4 4 6 8 8l2-3 6 2 1 5-3 2C13 27 3 17 4 7Z"/><path d="M17 8a6 6 0 0 1 5 5M17 3a11 11 0 0 1 10 10"/></svg>
  <div class="contact-label">PHONE</div>
  <div class="contact-info">+ (000) 555-0142</div>
</div>
<div class="abs contact-col" style="left:772px">
  <svg width="32" height="30" viewBox="0 0 32 30" fill="none" stroke="var(--white)" stroke-width="1.6"><rect x="2" y="5" width="28" height="20"/><path d="M2 5l14 12L30 5M2 25l11-10M30 25L19 15"/></svg>
  <div class="contact-label">EMAIL</div>
  <div class="contact-info">INFO@SKYVANE-DEMO.SE</div>
</div>

<div class="abs foot-link" style="left:238px">HOME</div>
<div class="abs foot-link" style="left:293px">ABOUT US</div>
<div class="abs foot-link" style="left:367px">CONTACT</div>
<div class="abs social-box" style="left:538px" aria-label="Social link"></div>
<div class="abs social-box" style="left:581px" aria-label="Social link"></div>
<div class="abs social-box" style="left:623px" aria-label="Social link"></div>
<div class="abs copyright">COPYRIGHT 2022. ALL RIGHT RESERVED.</div>

</body>
</html>
```